Healing Arts Brochure with Simple, Elegant, Zen Design ,

I need to create a brochure for an upcoming event and I have to complete this project in the next few days.
I would like a tri-fold or z fold type of brochure- standard size of 8.5 x 11- both sides with text

i would like the overall design to be simple, elegant and zen .... yet not too plain :-))
I would like the fonts used to be clean and clear and ... easy to read.
I would like the background color to be white/cream or light color
Please do not use too many colors when working with the descriptions of my services or break those sections up too much ... a little is ok.
I don't want the brochure to be busy

I've uploaded the text, my photo, a photo that I will be using on my website, my logo symbol without my name and several logo symbols with my name in different font styles. I am not wed to any of the various font styles of the logo just yet.
TEXT FILE IS UPLOADED

Dear Designers, The design submissions that I'm receiving so far have not been including all 3 pages of text in the brochure. I pulled my text file to update it with the instructions that there are 3 pages of text information that need to be on the brochure. Unfortunately, I'm not able to upload the text file - seems to be a glitch on the ArtMarkly website.. I called for support and they won't get back to me for a couple of hours. That will be around 11:00 am PST in the USA. PLEASE CHECK BACK if you haven't already downloaded the text file. Otherwise, please add the missing information and resubmit your ideas. Thank you!! MR

Target Market(s)

My services target clients in the healing arts.

Industry/Entity Type

Event

Requirements
Must have
• Please include the colors tones of my logo and the sunset photo -golds, oranges, blues
Brochure must include my photo and the sunset photo
Should not have
• Objects like teacups etc. that have nothing to do with my services - thank you kindly
I don't want any other photos or objects on the brochure other than my photo and the sun
Please don't put the tagline in quotes
Please do not make the brochure busy with too many colors in the text.

```html
<!DOCTYPE html>
<html lang="en">
<head>
<meta charset="utf-8">
<title>Maren Rowe – Healing Arts Brochure</title>
<link rel="stylesheet" href="https://fonts.googleapis.com/css2?family=Arimo:ital,wght@0,400;0,700;1,400&family=Tinos:ital,wght@0,400;0,700;1,400&display=swap">
<style>
  :root {
    --page-bg: #ffffff;
    --sun-gold: #fcc53a;
    --sun-amber: #f7ac2a;
    --sun-orange: #ee8c1c;
    --cream-soft: rgba(255, 240, 215, 0.88);
    --edge-orange: #f29a33;
    --tagline-blue: #1a9fd0;
    --heading-orange: #d86a12;
    --body-text: #5a4a3a;
    --quote-text: #3e3a36;
    --photo-tone: #a8a8a8;
  }
  * { box-sizing: border-box; margin: 0; padding: 0; }
  html, body { width: 1200px; height: 1000px; overflow: hidden; background: var(--page-bg); }
  .canvas { position: relative; width: 1200px; height: 1000px; }

  .spread { position: absolute; top: 237px; display: flex; height: 493px; box-shadow: 0 6px 18px rgba(0,0,0,0.12); }
  .spread--outside { left: 45px; }
  .spread--inside { left: 680px; }

  .panel { position: relative; height: 493px; overflow: hidden; }
  .panel--cover { width: 205px; }
  .panel--portrait, .panel--text { width: 213px; }

  .sunset {
    position: absolute; inset: 0;
    background: linear-gradient(180deg, var(--sun-amber) 0%, var(--sun-gold) 50%, var(--sun-orange) 100%);
  }
  .panel--text .sunset { opacity: 0.6; }

  .cover__tagline {
    position: absolute; left: 23px; width: 175px; top: 343px;
    font-family: "Tinos", serif; font-size: 18px; line-height: 21px;
    color: var(--tagline-blue);
  }

  .band {
    position: absolute; top: 0; bottom: 0; left: 4px; right: 14px;
    background: var(--cream-soft);
    border-left: 6px solid var(--edge-orange);
    border-right: 6px solid var(--edge-orange);
  }

  .portrait {
    position: absolute; left: 33px; width: 152px; top: 15px; height: 253px;
    background: var(--photo-tone);
  }
  .quote {
    position: absolute; left: 33px; width: 158px; top: 280px;
    font-family: "Arimo", sans-serif; font-style: italic; font-size: 11px; line-height: 16.5px;
    color: var(--quote-text);
  }
  .quote__author {
    position: absolute; right: 28px; top: 444px;
    font-family: "Arimo", sans-serif; font-style: italic; font-size: 11px; color: var(--quote-text);
  }

  .copy {
    position: absolute; left: 20px; width: 170px; top: 14px;
    font-family: "Arimo", sans-serif; font-size: 7px; line-height: 1.35; color: var(--body-text);
  }
  .copy h2 {
    font-family: "Tinos", serif; font-variant: small-caps; font-weight: 700;
    font-size: 11px; color: var(--heading-orange); margin: 0 0 4px;
  }
  .copy p { margin-bottom: 5px; }
  .copy .section-break { margin-top: 10px; }
  .symptoms { list-style: none; margin: 0 0 5px 12px; }
</style>
</head>
<body>
<main class="canvas">

  <section class="spread spread--outside" aria-label="Brochure outside">
    <article class="panel panel--cover">
      <div class="sunset" role="img" aria-label="Photograph of a golden sunset over the sea"></div>
      <p class="cover__tagline">Offerings to support you in discovering health, resiliency and well-being</p>
    </article>

    <article class="panel panel--portrait">
      <div class="sunset" role="img" aria-label="Sunset photograph continuing behind the panel"></div>
      <div class="band"></div>
      <div class="portrait" role="img" aria-label="Black and white portrait photograph of the practitioner"></div>
      <p class="quote">“The services that I offer focus on supporting self-care, self-empowerment and self-regulation. Healing is returning home to our inherent sense of resiliency, vitality and well-being. I am honored to work with you and support you in your own unique journey home to yourself!”</p>
      <p class="quote__author">Maren Rowe CMT, SEP</p>
    </article>
  </section>

  <section class="spread spread--inside" aria-label="Brochure inside">
    <article class="panel panel--text">
      <div class="sunset" role="img" aria-label="Soft sunset photograph behind the text"></div>
      <div class="band"></div>
      <div class="copy">
        <h2>Somatic Resourcing™</h2>
        <p>Somatic Resourcing is a body-oriented approach to the healing of trauma and other stress disorders. Sources of trauma include overwhelming events, accidents, loss, surgery, illness, falls and ongoing stress. Symptoms may appear long after the event and feel confusing.</p>
        <p>The symptoms of unresolved trauma include:</p>
        <ul class="symptoms">
          <li>Panic or anxiety including panic attacks</li>
          <li>Chronic pain of all kinds</li>
          <li>Sleep disorders</li>
          <li>Chronic fatigue</li>
          <li>Addictions of all kinds</li>
          <li>Migraines</li>
          <li>Gastrointestinal disorders</li>
          <li>Dissociation</li>
          <li>And many others</li>
        </ul>
        <p>Trauma occurs when the instinctual fight or flight states of our survival responses cannot complete. The result is energy remaining stuck or frozen within the body.</p>
        <p>Sessions assist clients to reconnect to their bodies and to gently discharge the stuck energies of trauma so that resiliency, stability and vitality are restored.</p>
        <p>I offer both Somatic Resourcing sessions and techniques in my private practice. I am deeply inspired and grateful for the results I have witnessed in my clients.</p>
      </div>
    </article>

    <article class="panel panel--text">
      <div class="sunset" role="img" aria-label="Soft sunset photograph behind the text"></div>
      <div class="band"></div>
      <div class="copy">
        <h2>Breath &amp; Yoga Nidra Meditation</h2>
        <p>Breath work has been known to support the nervous system and settle the mind. Yoga Nidra is a guided meditation practice that invites deep rest and awareness.</p>
        <p>I offer individual sessions to clients and small groups. The practice is gentle, accessible and requires no prior experience to enjoy.</p>
        <h2 class="section-break">Sound Therapy</h2>
        <p>For thousands of years cultures have used sound for healing. Vibration and tone help the body release tension and return to a balanced rhythm.</p>
        <p>The use of sound therapy can be a highly effective way to support healing. Singing bowls, gongs and voice are used to bring the body and mind into calm resonance and well-being.</p>
      </div>
    </article>
  </section>

</main>
</body>
</html>
```